IT Consulting company Needs a Logo Design and Business Cards

I need a New Logo and Business Cards for an established IT Managed Services Company that specializes in flat-rate managed IT services. We provide Design and Build, Help Desk, Onsite and Remote Support Services.

Target Market(s)

Corporate Clients

Industry/Entity Type

It Company

Logo Text

Halbrook Computer Group

Requirements
Nice to have
• Tag Line= Technology at Lightning Speed

```html
<!DOCTYPE html>
<html lang="en">
<head>
<meta charset="utf-8">
<title>Halbrook Computer Group – Business Cards</title>
<link rel="stylesheet" href="https://fonts.googleapis.com/css2?family=Montserrat:wght@400;500;700&family=Lato:wght@400;700&display=swap">
<style>
  :root {
    --stage: #2b2b2d;
    --navy-deep: #030640;
    --navy: #0a1a5c;
    --teal: #0a6d98;
    --sky: #27b6e8;
    --silver: #d8dde3;
    --white: #ffffff;
  }
  * { box-sizing: border-box; margin: 0; padding: 0; }
  html, body { width: 1200px; height: 900px; overflow: hidden; }
  body {
    background: var(--stage);
    font-family: "Lato", sans-serif;
    position: relative;
  }
  .card {
    position: absolute;
    left: 250px;
    width: 700px;
    height: 400px;
    overflow: hidden;
    box-shadow: 0 10px 30px rgba(0,0,0,.5);
  }
  .card--front {
    top: 40px;
    background: radial-gradient(ellipse at 50% 55%, var(--navy) 0%, var(--navy-deep) 70%);
    display: flex;
    align-items: center;
    justify-content: center;
  }
  .card--back { top: 460px; background: var(--white); }

  .wordmark {
    display: flex;
    align-items: center;
    gap: 14px;
    font-family: "Montserrat", sans-serif;
    font-weight: 700;
    letter-spacing: .02em;
    text-transform: uppercase;
    line-height: 1.15;
  }
  .wordmark__dot {
    width: 18px; height: 18px; border-radius: 50%;
    background: var(--sky);
    flex: none;
  }
  .wordmark__text { display: flex; flex-direction: column; }
  .card--front .wordmark { color: var(--sky); font-size: 34px; }
  .card--back .wordmark {
    position: absolute;
    left: 48px; top: 170px;
    color: var(--teal);
    font-size: 24px;
  }
  .card--back .wordmark__dot { width: 16px; height: 16px; }

  .back-art { position: absolute; inset: 0; }

  .contact {
    position: absolute;
    right: 36px; top: 36px;
    bottom: 32px;
    text-align: right;
    color: var(--white);
    display: flex;
    flex-direction: column;
  }
  .contact__name {
    font-family: "Montserrat", sans-serif;
    font-size: 27px;
    letter-spacing: .01em;
    color: var(--sky);
    line-height: 1;
  }
  .contact__name .first { font-weight: 400; }
  .contact__name .last { font-weight: 700; }
  .contact__role { font-size: 15px; letter-spacing: .06em; margin-top: 6px; }
  .contact__address { margin-top: 72px; font-size: 15px; line-height: 1.4; }
  .contact__lines { margin-top: auto; font-size: 14.5px; line-height: 1.55; }
  .contact__label { color: var(--sky); }
  .contact__web { font-weight: 700; }
</style>
</head>
<body>

<section class="card card--front" aria-label="Business card front">
  <div class="wordmark">
    <span class="wordmark__dot"></span>
    <span class="wordmark__text"><span>Halbrook</span><span>Computer Group</span></span>
  </div>
</section>

<section class="card card--back" aria-label="Business card back">
  <svg class="back-art" viewBox="0 0 700 400" width="700" height="400">
    <defs>
      <radialGradient id="panelGlow" cx="0.45" cy="0.4" r="0.75">
        <stop offset="0" stop-color="#0b7fae"/>
        <stop offset="0.55" stop-color="#084c88"/>
        <stop offset="1" stop-color="#061a5a"/>
      </radialGradient>
      <linearGradient id="bandTone" x1="0" y1="0" x2="0" y2="1">
        <stop offset="0" stop-color="#4fd0f5"/>
        <stop offset="1" stop-color="#0b5f95"/>
      </linearGradient>
      <linearGradient id="whiteFade" x1="0" y1="0" x2="1" y2="0">
        <stop offset="0.55" stop-color="#ffffff"/>
        <stop offset="1" stop-color="#e4e7ea"/>
      </linearGradient>
    </defs>
    <rect class="back-art__panel" width="700" height="400" fill="url(#panelGlow)"/>
    <path class="back-art__band" role="img" aria-label="Light blue band of overlapping translucent squares"
          d="M250 0 L345 0 Q445 200 370 400 L250 400 Z" fill="url(#bandTone)"/>
    <path class="back-art__rim" d="M250 0 L318 0 Q418 200 345 400 L250 400 Z" fill="var(--silver)"/>
    <path class="back-art__white" d="M0 0 L305 0 Q405 200 333 400 L0 400 Z" fill="url(#whiteFade)"/>
  </svg>

  <div class="wordmark">
    <span class="wordmark__dot"></span>
    <span class="wordmark__text"><span>Halbrook</span><span>Computer Group</span></span>
  </div>

  <div class="contact">
    <p class="contact__name"><span class="first">MARTIN </span><span class="last">CALDWELL</span></p>
    <p class="contact__role">CEO/President</p>
    <p class="contact__address">00 Quayside Ave. 0th Floor<br>Boston, MA 00000</p>
    <div class="contact__lines">
      <p><span class="contact__label">T.</span> (123) 555-0189</p>
      <p><span class="contact__label">E.</span> info@HalbrookComputerGroup.com</p>
      <p><span class="contact__label">W.</span> <span class="contact__web">HalbrookComputerGroup.com</span></p>
    </div>
  </div>
</section>

</body>
</html>
```